Business Card Design

My company is a health food catering and delivery business. Our colours are a bright turquiose green/blue, black, white and natural brown based beige. I would like the front of my card (working from the outside in; with a turquoise green boarder -quite thick, with a thin black line separating the turquoise boarder from the beige inside the remaining space of the front of the card with my logo in the centre. This should be all that appears on the front.

On the back I would like all the information displayed above on the beige coloured card, with the blurb in the bright turquoise and my contact information in black please. I would like my business name central - Harvest Crown Kitchen and immediately below with a right alignment - ...Dine like a Monarch
Below this should follow all that I have displayed above with a left alignment.

Target Market(s)

Cafes, restaurants, individuals, buying agents & super markets

Industry/Entity Type

Catering

Contact Information for Business Card

BACK OF BUSINESS CARD:
Harvest Crown Kitchen
...Dine like a Monarch
Deliciously healthy foods - free from gluten, lactose, cane sugar, trans-fat, GMO corn, soy & rice, no artificial flavours, colours or preservatives.
Prepared fresh from locally sourced ingredients, delivered to your door! For individuals, families, corporate, cafes, restaurants & event catering for Toowoomba & surrounds!

PH: 0491 538 207 // orders@harvestcrownkitchen.example
www.harvestcrownkitchen.example
www.socialpage.example/harvestcrownkitchen

Requirements
Must have
• Please supply a modern, easy to read text that will blend nicely with my logo text.
Nice to have
• I really want my business cards to stand out as these will be the template for brochures, menus and website designers to draw inspiration from!
Should not have
• Please do not use Arial, Tahoma or Times Roman text.

```html
<!DOCTYPE html>
<html lang="en">
<head>
<meta charset="utf-8">
<title>Harvest Crown Kitchen — Business Card Back</title>
<link rel="stylesheet" href="https://fonts.googleapis.com/css2?family=Cinzel:wght@700&family=Cabin:ital,wght@0,400;0,600;1,600&family=Archivo:wght@700&display=swap">
<style>
  :root {
    --turquoise: #1f9e99;
    --turquoise-text: #27a19d;
    --ink: #111111;
    --beige-light: #f7f6cf;
    --beige-mid: #eceab8;
    --beige-deep: #e2dfae;
    --shadow: rgba(40, 50, 40, 0.45);
  }
  html, body {
    margin: 0;
    padding: 0;
    width: 1200px;
    height: 716px;
    overflow: hidden;
    background: #ffffff;
  }
  .card {
    position: relative;
    width: 1200px;
    height: 716px;
    box-sizing: border-box;
    background: var(--turquoise);
    padding: 9px;
  }
  .card-face {
    position: relative;
    width: 100%;
    height: 100%;
    box-sizing: border-box;
    border: 2px solid var(--ink);
    background: linear-gradient(170deg, var(--beige-light) 0%, var(--beige-mid) 35%, var(--beige-light) 55%, var(--beige-deep) 80%, var(--beige-light) 100%);
    overflow: hidden;
  }
  .business-name {
    position: absolute;
    top: 42px;
    left: 0;
    width: 1180px;
    margin: 0;
    text-align: center;
    font-family: "Cinzel", serif;
    font-weight: 700;
    font-size: 60px;
    line-height: 1;
    color: var(--turquoise-text);
    text-shadow: 2px 2px 2px var(--shadow);
  }
  .tagline {
    position: absolute;
    top: 122px;
    right: 262px;
    margin: 0;
    font-family: "Cabin", sans-serif;
    font-style: italic;
    font-weight: 600;
    font-size: 47px;
    line-height: 1;
    color: var(--turquoise-text);
    text-shadow: 2px 2px 2px var(--shadow);
  }
  .blurb {
    position: absolute;
    top: 262px;
    left: 30px;
    margin: 0;
    font-family: "Cabin", sans-serif;
    font-weight: 600;
    font-size: 29px;
    line-height: 48px;
    letter-spacing: -0.2px;
    color: var(--turquoise-text);
    text-shadow: 1px 1px 1px var(--shadow);
    white-space: nowrap;
  }
  .contact {
    position: absolute;
    top: 570px;
    left: 0;
    width: 1180px;
    text-align: center;
    color: var(--ink);
  }
  .contact-phone {
    margin: 0;
    font-family: "Archivo", sans-serif;
    font-weight: 700;
    font-size: 32px;
    line-height: 46px;
  }
  .contact-line {
    margin: 0;
    font-family: "Cabin", sans-serif;
    font-weight: 400;
    font-size: 27px;
    line-height: 40px;
  }
</style>
</head>
<body>
  <div class="card">
    <div class="card-face">
      <h1 class="business-name">Harvest Crown Kitchen</h1>
      <p class="tagline">....Dine Like A Monarch</p>
      <p class="blurb">
        Deliciously healthy foods - free from gluten, lactose, cane sugar, trans-fat,<br>
        GMO corn, soy &amp; rice, no artificial flavours, colours or preservatives.<br>
        Prepared fresh from locally sourced ingredients, delivered to your door!<br>
        For individuals, families, corporate, cafes, restaurants &amp; event catering<br>
        for Toowoomba &amp; surrounds!
      </p>
      <div class="contact">
        <p class="contact-phone">PH: 0491 538 207</p>
        <p class="contact-line">orders@harvestcrownkitchen.example www.harvestcrownkitchen.example</p>
        <p class="contact-line">www.socialpage.example/harvestcrownkitchen</p>
      </div>
    </div>
  </div>
</body>
</html>
```